Website for premium health insurance and concierge medicine

This is a brand new website for Brask Insurance Services that specializes in Health Insurance and Concierge Medicine for high net-worth and affluent individuals and families. Through this website, clients will be able to learn about products and services, submit applications, and complete self enrollment forms. The website needs to have a premium look & feel that will appeal to a discerning high net-worth individual.

I’m looking for 4 pages in total to begin with. I’m also looking for a designer who will be interested in continuing to build out this new site further over the next few months.

The headline for each page is listed below:

Page 1: HOME PAGE
“Premium Healthcare | Bespoke Concierge Services | Absolute Peace of Mind.”

Page 2: HEALTH INSURANCE
“Premium Healthcare | Elevated.”

Page 3: CONCIERGE MEDICINE
“Personalized Medicine | At-Home Concierge Care | Your Private Physician, 24/7.”

Page 4: DENTAL & VISION
“Your Smile | Your Vision | Perfected.”

Here are several links to existing websites that can be used as design inspiration:

https://vantromhealth.com
https://www.pelvix.org/specialties-services/other-programs-services/concierge-medicine
https://wardelmdnx.com

More generally speaking, I like a clean, modern, dutch style of websites. Here’s an unrelated site that has a good design:

https://www.morvathis.com

Here are a few additional phrases and keywords that will help inspire the design:

Premium Health Insurance
Executive Health Insurance
Concierge Medicine
24/7 access dedicated concierge team
Integrative Concierge Care

I will upload logo files below, here are the font & colors information:

Font: Trajan Pro Bold
Colors:
Blue: hex code: 0071BD, Rgb code: 0, 113, 189  cmyk code: 87,53,0,0
Gray: hex code: #666666, Rgb code: 102,102,102 cmyk code: 60,51,51,20

```html
<!DOCTYPE html>
<html lang="en">
<head>
<meta charset="utf-8">
<title>Brask Insurance Services — Health Coverage</title>
<link rel="stylesheet" href="https://fonts.googleapis.com/css2?family=Libre+Baskerville:wght@400;700&family=Open+Sans:wght@400;600;700;800&display=swap">
<style>
:root{
  --blue:#0071BD;
  --blue-dark:#0a5ea3;
  --navy:#14203f;
  --navy-soft:#1f2b4d;
  --gray:#666666;
  --text:#1a1a1a;
  --orange:#e2782e;
  --footer:#252a37;
  --footer-deep:#1c2030;
  --field:#eef0f7;
  --white:#ffffff;
  --teal:#2f9fb5;
}
*{margin:0;padding:0;box-sizing:border-box}
html,body{width:1200px;height:4246px;overflow:hidden}
body{position:relative;background:var(--white);font-family:"Open Sans",Arial,sans-serif;color:var(--text)}
.abs{position:absolute}
.label{font-size:12.5px;color:var(--blue);text-decoration:underline;text-underline-offset:4px;letter-spacing:.2px}
.section-title{font-family:"Libre Baskerville",Georgia,serif;font-weight:700;font-size:42px;color:var(--navy);text-align:center;width:1200px;left:0}

/* header */
.update-bar{left:214px;top:0;width:986px;height:36px;background:#f3f3f3;font-size:12.5px;color:#444;display:flex;align-items:center;padding-left:44px}
.update-bar .tag{color:var(--orange);font-weight:700;margin:0 8px 0 10px}
.update-icon{width:16px;height:12px;border:1.5px solid var(--orange);border-radius:2px}
.logo{left:50px;top:22px;display:flex;align-items:center;gap:8px}
.logo-mark{width:46px;height:46px;border-radius:50%;background:var(--blue)}
.logo-name{font-weight:700;font-size:13px;line-height:15px;color:var(--blue);width:96px}
.nav{left:214px;top:36px;width:986px;height:76px;background:var(--white);box-shadow:0 2px 6px rgba(0,0,0,.08)}
.nav ul{list-style:none;position:absolute;left:28px;top:32px;display:flex}
.nav li{font-size:11.5px;font-weight:700;color:var(--navy);margin-right:37px}
.nav li.active{color:var(--blue)}
.phone-badge{left:959px;top:51px;width:46px;height:46px;border-radius:50%;background:#3a3f4a;display:flex;align-items:center;justify-content:center}
.enquiry{left:1022px;top:56px}
.enquiry small{display:block;font-size:11px;font-weight:700;color:var(--orange)}
.enquiry strong{display:block;font-size:14.5px;color:var(--navy);margin-top:4px}

/* hero */
.hero{left:0;top:112px;width:1200px;height:700px;background:linear-gradient(100deg,#27385f 0%,#4a5a7c 40%,#8d8f98 70%,#b9b6b3 100%)}
.hero-title{left:90px;top:264px;width:568px;height:79px;background:linear-gradient(90deg,rgba(255,255,255,.28),rgba(255,255,255,.08) 75%,rgba(255,255,255,.3));border-right:2px solid rgba(255,255,255,.5)}
.hero-title h1{font-family:"Libre Baskerville",Georgia,serif;font-weight:700;font-size:51px;color:var(--white);position:absolute;left:15px;top:6px;white-space:nowrap}
.hero-sub{left:90px;top:354px;width:560px;font-size:20px;font-weight:700;line-height:29px;color:var(--white)}
.btn-pill{left:89px;top:445px;width:266px;height:45px;border-radius:23px;background:var(--blue);color:var(--white);font-size:13px;font-weight:700;display:flex;align-items:center;justify-content:center}

/* about */
.about-photo{left:94px;top:808px;width:390px;height:390px;border-radius:50%;background:linear-gradient(135deg,#a68a6c,#d8c7b1 55%,#9aa3ab);overflow:hidden}
.about-ring{left:120px;top:812px;width:400px;height:400px;border-radius:50%;background:#e3efe4}
.about-small{left:424px;top:848px;width:140px;height:185px;border-radius:50%;background:linear-gradient(160deg,#e5e6e8,#7b858f)}
.about-dot{left:100px;top:1100px;width:96px;height:96px;border-radius:50%;background:var(--blue)}
.about-text{left:630px;top:766px;width:505px}
.about-text h2{font-family:"Libre Baskerville",Georgia,serif;font-weight:700;font-size:42px;line-height:54px;color:var(--navy);margin-top:16px}
.about-text .lead{font-family:"Libre Baskerville",Georgia,serif;font-size:22px;color:var(--navy);margin-top:20px}
.about-text p{font-size:13.3px;line-height:21.6px;color:var(--gray);margin-top:16px}
.btn-contact{left:630px;top:1139px;width:154px;height:44px;background:var(--blue);color:var(--white);font-weight:700;font-size:15px;display:flex;align-items:center;justify-content:center;gap:14px;border-radius:2px;z-index:5}

/* services */
.services-bg{left:0;top:1290px;width:1200px;height:580px;background:linear-gradient(90deg,#c9ccd3,#dfe1e6 45%,#cfd2d8)}
.accent{background:var(--navy)}
.card{background:var(--white);text-align:center;padding-top:40px;box-shadow:0 4px 14px rgba(0,0,0,.08)}
.card h3{font-family:"Libre Baskerville",Georgia,serif;font-weight:700;font-size:17px;color:var(--navy);margin-top:14px}
.card .rule{width:26px;height:3px;background:var(--blue);margin:12px auto 0}
.card p{font-size:12px;line-height:20px;color:var(--gray);width:240px;margin:12px auto 0}
.card .more{font-size:11px;font-weight:700;color:#444;margin-top:14px;display:block}
.card.featured{background:linear-gradient(160deg,#3c4b78,#232f57 60%,#1b2549);padding-top:62px}
.card.featured h3,.card.featured p{color:var(--white)}
.card.featured .more{display:inline-block;color:var(--white);border:1.5px solid var(--white);width:138px;height:34px;line-height:31px;margin-top:18px}

/* testimonials */
.avatar{border-radius:50%;border:3px solid var(--white);box-shadow:0 3px 10px rgba(0,0,0,.15)}
.quote{left:0;top:2291px;width:1200px;text-align:center;font-size:18.5px;line-height:31px;color:var(--gray)}
.stars{left:0;top:2394px;width:1200px;text-align:center;color:#f08a1c;font-size:19px;letter-spacing:2px}
.reviewer{left:0;top:2424px;width:1200px;text-align:center;font-size:17px;font-weight:700;color:#555;letter-spacing:.4px}
.reviewer-role{left:0;top:2454px;width:1200px;text-align:center;font-size:9.5px;color:#666;font-weight:600}
.arrow-btn{width:46px;height:46px;border-radius:50%;display:flex;align-items:center;justify-content:center}

/* team */
.team-bg{left:0;top:2546px;width:1200px;height:620px;background:linear-gradient(90deg,#cdd0d6,#e2e4e9 50%,#cfd2d8)}
.member{width:218px;height:305px;background:var(--white);box-shadow:0 4px 12px rgba(0,0,0,.08)}
.member .photo{width:218px;height:218px}
.member .plus{position:absolute;left:181px;top:202px;width:30px;height:30px;background:var(--white);display:flex;align-items:center;justify-content:center;font-size:15px;color:#444}
.member small{position:absolute;left:22px;top:244px;font-size:9.5px;color:var(--blue)}
.member strong{position:absolute;left:22px;top:262px;font-size:15.5px;color:#222}
.member.dark{background:#2d3038}
.member.dark small{color:#ddd}
.member.dark strong{color:var(--white)}
.social-stack{position:absolute;left:162px;top:14px;display:flex;flex-direction:column;gap:10px}
.social-stack span{width:30px;height:30px;background:var(--white);display:block}
.social-stack span.on{background:var(--blue)}
.social-stack span.add{background:var(--blue);color:var(--white);font-size:18px;text-align:center;line-height:29px}

/* contact */
.touch-title{left:132px;top:3300px;font-size:33px;color:var(--navy);letter-spacing:.5px;font-weight:400}
.touch-title b{font-weight:800}
.touch-intro{left:134px;top:3350px;width:400px;font-size:11.8px;line-height:23px;color:#444}
.info-icon{width:42px;height:42px;border-radius:50%;background:var(--blue);display:flex;align-items:center;justify-content:center}
.info-block h4{font-size:13px;font-weight:700;color:var(--navy)}
.info-block p{font-size:13px;line-height:23px;color:#333}
.round-social{width:40px;height:40px;border-radius:50%;background:var(--navy)}
.message-box{left:593px;top:3283px;width:482px;height:392px;border:2px solid #d6d8de;border-radius:6px;background:var(--white)}
.message-box h3{position:absolute;left:38px;top:34px;font-size:19.5px;font-weight:700;color:var(--navy-soft)}
.field{position:absolute;left:34px;width:414px;background:var(--field);border-radius:3px;font-size:11.5px;color:#333;padding:15px 0 0 24px}
.send{position:absolute;left:34px;top:304px;width:414px;height:48px;background:var(--blue);color:var(--white);font-size:16.5px;font-weight:700;display:flex;align-items:center;justify-content:center;border-radius:2px}

/* footer */
.footer{left:0;top:3733px;width:1200px;height:466px;background:var(--footer)}
.footer-form{left:102px;top:3804px;width:313px;height:324px;background:var(--footer-deep);border-top:3px solid var(--blue);border-radius:2px}
.footer-form h4{position:absolute;left:22px;top:20px;font-size:18px;color:var(--white);font-weight:700}
.footer-field{position:absolute;left:24px;width:261px;height:46px;border:1px solid #3b4152;background:#262b39;color:var(--white);font-size:12px;font-weight:600;padding:15px 0 0 14px}
.footer-submit{position:absolute;left:24px;top:251px;width:261px;height:50px;background:var(--blue);color:var(--white);font-size:11px;font-weight:700;display:flex;align-items:center;justify-content:center}
.footer-col h4{font-size:18.5px;font-weight:700;color:var(--white)}
.footer-col ul{list-style:none;margin-top:28px}
.footer-col li{font-size:13px;color:var(--white);font-weight:600;line-height:31px}
.footer-col li::before{content:"- ";color:#ccc}
.subscribe-text{font-size:13px;line-height:22px;color:var(--white);font-weight:600}
.subscribe-field{left:785px;top:3950px;width:311px;height:44px;background:#2f3443;border-radius:3px}
.subscribe-field span{position:absolute;left:16px;top:13px;font-size:13px;color:var(--white);font-weight:600}
.subscribe-btn{position:absolute;right:0;top:0;width:74px;height:44px;background:var(--blue);border-radius:3px;display:flex;align-items:center;justify-content:center}
.foot-social{width:34px;height:34px;border-radius:50%;background:#3a3f4e}
.to-top{left:1115px;top:4139px;width:39px;height:39px;border-radius:50%;border:2px solid var(--blue);display:flex;align-items:center;justify-content:center}
.bottom-bar{left:0;top:4199px;width:1200px;height:47px;background:var(--blue);color:var(--white);font-size:14px;font-weight:600}
.bottom-bar span{position:absolute;top:14px}
</style>
</head>
<body>

<!-- Header -->
<div class="abs update-bar"><span class="update-icon"></span><span class="tag">UPDATES:</span>Lorem ipsum dolor sit amet, consectetur adipiscing elit, sed do eiusmod tempor incididunt ut labore et dolore magna aliqua.</div>
<div class="abs logo"><span class="logo-mark"></span><span class="logo-name">Brask Insurance Services</span></div>
<nav class="abs nav">
  <ul>
    <li class="active">HOME</li><li>ABOUT US</li><li>SERVICES</li><li>PROJECTS</li><li>BLOG</li><li>CONTACT</li>
  </ul>
</nav>
<div class="abs phone-badge">
  <svg width="20" height="20" viewBox="0 0 24 24"><path d="M6.6 10.8a15 15 0 0 0 6.6 6.6l2.2-2.2c.3-.3.7-.4 1-.2 1.1.4 2.3.6 3.6.6.6 0 1 .4 1 1V20c0 .6-.4 1-1 1A17 17 0 0 1 3 4c0-.6.4-1 1-1h3.5c.6 0 1 .4 1 1 0 1.3.2 2.5.6 3.6.1.3 0 .7-.2 1z" fill="#fff"/></svg>
</div>
<div class="abs enquiry"><small>ENQUIRIES</small><strong>+ 1-888-555-01-234</strong></div>

<!-- Hero -->
<section class="abs hero" role="img" aria-label="Photo of business people networking at a corporate event, seen from above"></section>
<div class="abs hero-title"><h1>Health Coverage</h1></div>
<p class="abs hero-sub">Lorem ipsum dolor sit amet, consectetur adipiscing elit, sed do eiusmod tempor incididunt ut labore</p>
<div class="abs btn-pill">SCHEDULE A FREE CONSULT</div>
<svg class="abs" style="left:0;top:620px" width="1200" height="200" viewBox="0 0 1200 200">
  <path d="M0,172 C300,60 650,35 1200,75 L1200,200 L0,200 Z" fill="#fff"/>
  <path d="M0,150 C300,48 650,24 1200,75 C650,40 300,75 0,190 Z" fill="#0071BD"/>
</svg>

<!-- About -->
<div class="abs about-ring"></div>
<div class="abs about-photo" role="img" aria-label="Photo of a team meeting around a wooden table with laptops, seen from above"></div>
<div class="abs about-small" role="img" aria-label="Photo of a woman presenting charts on a board"></div>
<div class="abs about-dot"></div>
<div class="abs about-text">
  <span class="label">WHO WE ARE</span>
  <h2>Health insurance you can trust.</h2>
  <div class="lead">Reliable coverage, for a healthier you.</div>
  <p>Lorem ipsum dolor sit amet, consectetur adipiscing elit, sed do eiusmod tempor incididunt ut labore et dolore magna aliqua. Ut enim ad minim veniam, quis nos trud exercitation ullamco laboris nisi ut aliquip ex ea commodo consequat.<br>Duis aute irure dolor in reprehenderit in voluptate velit esse cillum dolore eu fugiat nulla pariatur. Excepteur sint occaecat cupidatat non proident, sunt in culpa qui officia deserunt mollit anim id est laborum.</p>
</div>

<!-- Services -->
<section class="abs services-bg" role="img" aria-label="Faded photo of a busy office lobby with people walking"></section>
<svg class="abs" style="left:0;top:1150px" width="1200" height="190" viewBox="0 0 1200 190">
  <path d="M0,0 H1200 V20 C1050,120 800,170 450,178 C300,180 150,165 0,150 Z" fill="#fff"/>
  <path d="M1200,20 C1050,120 800,170 450,178 C820,182 1080,118 1200,58 Z" fill="#0071BD"/>
</svg>
<div class="abs btn-contact">Contact us
  <svg width="18" height="14" viewBox="0 0 18 14"><path d="M1 7h15M10 1l6 6-6 6" stroke="#fff" stroke-width="2" fill="none"/></svg>
</div>
<span class="abs label" style="left:0;top:1401px;width:1200px;text-align:center">OUR SERVICES</span>
<h2 class="abs section-title" style="top:1436px">Services We Offer</h2>

<div class="abs accent" style="left:122px;top:1541px;width:90px;height:262px"></div>
<div class="abs accent" style="left:990px;top:1660px;width:90px;height:152px"></div>

<div class="abs card" style="left:135px;top:1552px;width:290px;height:253px">
  <svg width="40" height="40" viewBox="0 0 40 40"><path d="M20 4 L33 11 L35 25 L26 35 L14 35 L5 25 L7 11 Z" fill="none" stroke="#0071BD" stroke-width="2.5" stroke-linejoin="round"/></svg>
  <h3>Health Insurance</h3><div class="rule"></div>
  <p>Lorem ipsum dolor sit amet, consectetur adipiscing elit, sed do adipiscing elit, sed do</p>
  <span class="more">LEARN MORE</span>
</div>
<div class="abs card featured" style="left:451px;top:1531px;width:301px;height:293px" role="img" aria-label="Concierge Medicine card over a dark blue photo of office workers">
  <svg width="40" height="40" viewBox="0 0 40 40"><path d="M20 4 L33 11 L35 25 L26 35 L14 35 L5 25 L7 11 Z" fill="none" stroke="#fff" stroke-width="2.5" stroke-linejoin="round"/></svg>
  <h3>Concierge Medicine</h3>
  <p>Lorem ipsum dolor sit amet, consectetur adipiscing elit, sed do adipiscing elit, sed do</p>
  <span class="more">LEARN MORE</span>
</div>
<div class="abs card" style="left:780px;top:1552px;width:291px;height:253px">
  <svg width="40" height="40" viewBox="0 0 40 40"><path d="M20 4 L33 11 L35 25 L26 35 L14 35 L5 25 L7 11 Z" fill="none" stroke="#0071BD" stroke-width="2.5" stroke-linejoin="round"/></svg>
  <h3>Dental and Vision</h3><div class="rule"></div>
  <p>Lorem ipsum dolor sit amet, consectetur adipiscing elit, sed do adipiscing elit, sed do</p>
  <span class="more">LEARN MORE</span>
</div>

<!-- Testimonials -->
<span class="abs label" style="left:0;top:1938px;width:1200px;text-align:center">TESTIMONIALS</span>
<h2 class="abs section-title" style="top:1974px">Clients' Feedback</h2>
<svg class="abs" style="left:0;top:2050px" width="1200" height="260" viewBox="0 2050 1200 260">
  <path d="M198,2279 Q603,1980 1009,2279" fill="none" stroke="#2f9fb5" stroke-width="2" stroke-dasharray="9 7"/>
</svg>
<div class="abs avatar" style="left:544px;top:2070px;width:118px;height:118px;background:linear-gradient(160deg,#e4e4e4,#8a8f96)" role="img" aria-label="Client portrait"></div>
<div class="abs avatar" style="left:343px;top:2124px;width:76px;height:76px;background:linear-gradient(160deg,#f1e4da,#c9b3a3)" role="img" aria-label="Client portrait"></div>
<div class="abs avatar" style="left:786px;top:2124px;width:76px;height:76px;background:linear-gradient(160deg,#c7a27f,#6a4a36)" role="img" aria-label="Client portrait"></div>
<div class="abs avatar" style="left:160px;top:2241px;width:76px;height:76px;background:linear-gradient(160deg,#f0e6df,#b99b85)" role="img" aria-label="Client portrait"></div>
<div class="abs avatar" style="left:971px;top:2241px;width:76px;height:76px;background:linear-gradient(160deg,#ececec,#8a7a70)" role="img" aria-label="Client portrait"></div>
<svg class="abs" style="left:581px;top:2225px" width="40" height="32" viewBox="0 0 40 32"><path d="M2 32V18C2 8 6 3 16 0l2 4C12 6 10 10 10 14h8v18zM22 32V18c0-10 4-15 14-18l2 4c-6 2-8 6-8 10h8v18z" fill="#14203f"/></svg>
<p class="abs quote">Lorem ipsum dolor sit amet, consectetur adipiscing elit, sed do eiusmod tem<br>por incididunt ut labore et dolore magna aliqua. Ut enim ad minim veniam.<br>labore et dolore magna aliq</p>
<div class="abs stars">★★★★★</div>
<div class="abs reviewer">Dorian Wells</div>
<div class="abs reviewer-role">Client</div>
<div class="abs arrow-btn" style="left:465px;top:2409px;background:var(--navy)"><svg width="12" height="14" viewBox="0 0 12 14"><path d="M9 1 3 7l6 6" stroke="#fff" stroke-width="2.2" fill="none"/></svg></div>
<div class="abs arrow-btn" style="left:695px;top:2409px;background:var(--blue)"><svg width="12" height="14" viewBox="0 0 12 14"><path d="M3 1l6 6-6 6" stroke="#fff" stroke-width="2.2" fill="none"/></svg></div>

<!-- Team -->
<section class="abs team-bg" role="img" aria-label="Faded photo of a busy office lobby with people walking"></section>
<span class="abs label" style="left:0;top:2606px;width:1200px;text-align:center">OUR TEAM</span>
<h2 class="abs section-title" style="top:2641px">Meet Our Team</h2>

<div class="abs member" style="left:122px;top:2745px">
  <div class="photo" role="img" aria-label="Portrait of a team member holding a tablet" style="background:linear-gradient(160deg,#3d556f,#6f7f90 60%,#2f4560)"></div>
  <span class="plus">+</span><small>Founder</small><strong>Rowan D. Ellery</strong>
</div>
<div class="abs member dark" style="left:366px;top:2745px">
  <div class="photo" role="img" aria-label="Portrait of a smiling team member with glasses" style="background:linear-gradient(160deg,#e8e9eb,#9a9ea5 60%,#55585f)"></div>
  <div class="social-stack"><span class="on"></span><span></span><span></span><span></span><span class="add">+</span></div>
  <small>Founder</small><strong>Rowan D. Ellery</strong>
</div>
<div class="abs member" style="left:615px;top:2745px">
  <div class="photo" role="img" aria-label="Portrait of a team member in a dark blazer" style="background:linear-gradient(160deg,#b7c0ca,#5b6673 55%,#1f2630)"></div>
  <span class="plus">+</span><small>Founder</small><strong>Rowan D. Ellery</strong>
</div>
<div class="abs member" style="left:859px;top:2745px">
  <div class="photo" role="img" aria-label="Portrait of a team member holding a tablet in an office" style="background:linear-gradient(160deg,#e8e4de,#b5a89a 55%,#6b5a4a)"></div>
  <span class="plus">+</span><small>Founder</small><strong>Rowan D. Ellery</strong>
</div>

<svg class="abs" style="left:0;top:3080px" width="1200" height="200" viewBox="0 0 1200 200">
  <path d="M0,200 L0,180 C300,80 600,40 1200,42 L1200,200 Z" fill="#fff"/>
  <path d="M0,160 C300,62 600,30 860,34 C600,42 300,90 0,195 Z" fill="#0071BD"/>
</svg>

<!-- Get in touch -->
<h2 class="abs touch-title">GET IN <b>TOUCH</b></h2>
<p class="abs touch-intro">Lorem ipsum dolor sit amet, consectetur adipiscing elit, sed do eiu smod tempor incididunt ut labore et dolore magna aliqua.</p>
<div class="abs info-icon" style="left:127px;top:3427px">
  <svg width="16" height="20" viewBox="0 0 16 20"><path d="M8 0a8 8 0 0 0-8 8c0 6 8 12 8 12s8-6 8-12a8 8 0 0 0-8-8zm0 11a3 3 0 1 1 0-6 3 3 0 0 1 0 6z" fill="#fff"/></svg>
</div>
<div class="abs info-block" style="left:187px;top:3427px"><h4>CORVANE OFFICE</h4><p>48 Harlow Lane,<br>Suite 310, Corvane, Cv204</p></div>
<div class="abs info-icon" style="left:127px;top:3522px">
  <svg width="18" height="18" viewBox="0 0 24 24"><path d="M6.6 10.8a15 15 0 0 0 6.6 6.6l2.2-2.2c.3-.3.7-.4 1-.2 1.1.4 2.3.6 3.6.6.6 0 1 .4 1 1V20c0 .6-.4 1-1 1A17 17 0 0 1 3 4c0-.6.4-1 1-1h3.5c.6 0 1 .4 1 1 0 1.3.2 2.5.6 3.6.1.3 0 .7-.2 1z" fill="#fff"/></svg>
</div>
<div class="abs info-block" style="left:187px;top:3525px"><h4>PHONE NUMBER</h4><p style="line-height:18px">+213 555- 0147</p></div>
<div class="abs round-social" style="left:133px;top:3601px"></div>
<div class="abs round-social" style="left:180px;top:3601px"></div>
<div class="abs round-social" style="left:227px;top:3601px"></div>

<div class="abs message-box">
  <h3>LEAVE US A MESSAGE</h3>
  <div class="field" style="top:76px;height:43px">Email address</div>
  <div class="field" style="top:138px;height:43px">Subject</div>
  <div class="field" style="top:198px;height:95px">Write Your Message Here</div>
  <div class="send">SEND MESSAGE</div>
</div>

<!-- Footer -->
<footer class="abs footer"></footer>
<div class="abs footer-form">
  <h4>Contact Us</h4>
  <div class="footer-field" style="top:59px">Enter Your Name</div>
  <div class="footer-field" style="top:122px">Enter Your Mail</div>
  <div class="footer-field" style="top:185px">Enter Your Subject</div>
  <div class="footer-submit">SUBMIT</div>
</div>
<div class="abs footer-col" style="left:442px;top:3829px">
  <h4>Informations</h4>
  <ul><li>How it Works</li><li>Partners</li><li>Testimonials</li><li>Key Areas</li><li>Case Studies</li><li>Pricing</li></ul>
</div>
<div class="abs footer-col" style="left:601px;top:3829px">
  <h4 style="visibility:hidden">Links</h4>
  <ul><li>Careers</li><li>Infrastructure</li><li>Client Support</li><li>Privacy Policy</li><li>Terms of Use</li><li>Sitemap</li></ul>
</div>
<div class="abs footer-col" style="left:783px;top:3829px;width:330px">
  <h4>Informations</h4>
  <p class="subscribe-text" style="margin-top:30px">Subscribe to us &amp; receive our offers and updates in your inbox directly</p>
</div>
<div class="abs subscribe-field"><span>Your Email Address</span>
  <div class="subscribe-btn"><svg width="18" height="14" viewBox="0 0 18 14"><path d="M1 7h15M10 1l6 6-6 6" stroke="#fff" stroke-width="2" fill="none"/></svg></div>
</div>
<p class="abs subscribe-text" style="left:785px;top:4018px">* We do not share your email id</p>
<div class="abs foot-social" style="left:785px;top:4065px"></div>
<div class="abs foot-social" style="left:834px;top:4065px"></div>
<div class="abs foot-social" style="left:882px;top:4065px"></div>
<div class="abs foot-social" style="left:931px;top:4065px"></div>
<div class="abs to-top"><svg width="14" height="10" viewBox="0 0 14 10"><path d="M1 8l6-6 6 6" stroke="#0071BD" stroke-width="2" fill="none"/></svg></div>
<div class="abs bottom-bar"><span style="left:115px">Brask Insurance Services</span><span style="right:102px">Privacy Policy</span></div>

</body>
</html>
```